Photographic Tutorial website

We are looking for a fresh design for a photographic tutorial / workshop website. The website will have the included functions:

* Home (needs to have a login section)
* About Us
* Info about each course / workshop.
* Subscribe to courses and pay online.
* Members Area
* Photo gallery
* Contact us

The website will be implemented with our own made cms. We do not need it to be coded. We have a team ready to do this for us. We only need the PSD layout.

We have attached a mockup design that the client and I have come up with and we need the design to be taken to the next level.

Client also likes:
http://www.vellowindstudio.example/

Photographic Interests

Online

Requirements
Must have
• Must Stand out i.e black backgrounds
Should not have
• Alter the logo in anyway.

```html
<!DOCTYPE html>
<html lang="en">
<head>
<meta charset="utf-8">
<title>Lens Compass – Photographic Tuition</title>
<link href="https://fonts.googleapis.com/css2?family=Arimo:wght@400;700&display=swap" rel="stylesheet">
<style>
:root{
  --black:#000;
  --panel:#1f1f1f;
  --panel-dark:#151515;
  --nav:#232323;
  --nav-line:#333;
  --red:#e01f26;
  --red-deep:#9e0b0f;
  --red-dark:#5c0407;
  --white:#fff;
  --grey:#8a8a8a;
  --grey-dark:#555;
  --sand:#c9ad8a;
}
*{margin:0;padding:0;box-sizing:border-box}
html,body{width:889px;height:1200px;overflow:hidden;background:var(--black)}
body{font-family:"Arimo",Arial,sans-serif;color:var(--white);position:relative}
.abs{position:absolute}

/* header */
.sidebar{left:0;top:0;width:284px;height:373px;background:var(--nav)}
.brand{left:0;top:0;width:284px;height:107px;background:#111;display:flex;align-items:center;padding-left:10px;gap:9px}
.brand-dot{width:30px;height:30px;border-radius:50%;background:var(--red);flex:none}
.brand-text{display:flex;flex-direction:column}
.brand-name{font-size:29px;font-weight:700;color:var(--white);line-height:1}
.brand-tag{font-size:11px;color:var(--white);letter-spacing:2.2px;margin-top:3px}
.nav{left:0;top:107px;width:284px;list-style:none}
.nav li{height:44.4px;line-height:44px;padding-left:17px;font-size:13px;font-weight:700;border-bottom:1px solid var(--nav-line)}
.nav li.active{background:var(--red);width:284px}
.hero{left:284px;top:0;width:605px;height:373px;background:linear-gradient(180deg,#9da4a7 0%,#d8c3a4 25%,var(--sand) 60%,#b89a78 100%)}
.hero-badge{left:724px;top:7px;width:156px;height:69px;background:rgba(20,20,20,.82);text-align:center;padding-top:11px}
.hero-badge b{display:block;font-size:22px;letter-spacing:.5px}
.hero-badge span{display:block;font-size:18px;font-weight:700;color:var(--red)}

/* gallery strip */
.strip{left:7px;top:413px;width:876px;height:158px;background:var(--white)}
.thumb{top:424px;width:135px;height:133px}
.thumb .pic{height:103px}
.thumb .cap{height:30px;background:var(--red-deep);font-size:12px;font-weight:700;text-align:center;line-height:30px}
.arrow{top:471px;width:26px;height:40px;background:var(--white);border:1px solid #ccc}
.arrow.left{left:7px;border-radius:0 20px 20px 0}
.arrow.right{left:857px;border-radius:20px 0 0 20px}
.reflect{top:573px;width:135px;height:54px;opacity:.18;background:linear-gradient(180deg,#666,transparent)}

/* content */
.content{left:0;top:627px;width:889px;height:500px;background:var(--panel)}
.heading{font-size:15px;font-weight:700}
.caption{background:var(--red-deep);font-size:11px;line-height:16px;padding:6px 9px}
.caption em{font-style:normal;font-weight:700;float:right;color:#111}
.links{left:9px;top:956px;width:235px;height:147px;background:linear-gradient(90deg,var(--red-dark),var(--red-deep) 60%,#c41218);list-style:none;padding-top:7px}
.links li{height:27px;line-height:27px;font-size:12px;font-weight:700;padding-left:22px;position:relative}
.links li::before{content:"";position:absolute;left:11px;top:11px;border:4px solid transparent;border-left:5px solid #111}
.post{left:277px;width:339px}
.post-title{font-size:12px;color:var(--red)}
.post-date{position:absolute;right:12px;top:0;font-size:10px}
.post-text{font-size:10.5px;color:var(--grey-dark);line-height:17px;margin-top:7px;padding-bottom:10px;border-bottom:1px solid #333}
.checks{left:640px;top:960px;width:232px;height:87px;background:linear-gradient(90deg,#c41218,var(--red-dark));list-style:none;padding:10px 0 0 12px}
.checks li{display:flex;align-items:center;gap:12px;height:23px;font-size:11.5px;font-weight:700;color:#111}

/* footer */
.footer{left:0;top:1127px;width:889px;height:73px;background:var(--black)}
.foot-brand{left:16px;top:1146px;display:flex;align-items:center;gap:10px}
.foot-dot{width:34px;height:34px;border-radius:50%;background:var(--red)}
.foot-name{font-size:13px;font-weight:700}
.foot-copy{left:90px;top:1158px;font-size:9.5px;color:var(--grey)}
.follow{left:635px;top:1143px;width:229px;height:41px;background:#222;border:1px solid #444;font-size:16px;font-weight:700;color:#bbb;letter-spacing:1px;line-height:39px;padding-left:14px}
</style>
</head>
<body>

<div class="abs sidebar"></div>
<div class="abs brand">
  <div class="brand-dot"></div>
  <div class="brand-text">
    <span class="brand-name">Lens Compass</span>
    <span class="brand-tag">PHOTOGRAPHIC TUITION</span>
  </div>
</div>
<ul class="abs nav">
  <li class="active">HOME</li>
  <li>ABOUT US</li>
  <li>COURSE/WORKSHOP INFO</li>
  <li>MEMBERS AREA</li>
  <li>PHOTO GALLERY</li>
  <li>CONTACT US</li>
</ul>
<div class="abs hero" role="img" aria-label="Photographer lying on desert sand shooting with a camera"></div>
<div class="abs hero-badge"><b>WILD LIFE</b><span>photography</span></div>

<div class="abs strip"></div>
<div class="abs thumb" style="left:19px"><div class="pic" role="img" aria-label="Stone alley in an old town" style="background:linear-gradient(160deg,#b9ab97,#7d7264)"></div><div class="cap">Urber Photography</div></div>
<div class="abs thumb" style="left:162px"><div class="pic" role="img" aria-label="Animal among dry branches" style="background:linear-gradient(160deg,#6b5646,#3a2c22)"></div><div class="cap">Urber Photography</div></div>
<div class="abs thumb" style="left:305px"><div class="pic" role="img" aria-label="Country road under blue sky" style="background:linear-gradient(180deg,#6d9ac8,#c8b27a 60%,#8f7a4a)"></div><div class="cap">Urber Photography</div></div>
<div class="abs thumb" style="left:448px"><div class="pic" role="img" aria-label="Black and white antelope with horns" style="background:linear-gradient(160deg,#999,#2c2c2c)"></div><div class="cap">Urber Photography</div></div>
<div class="abs thumb" style="left:591px"><div class="pic" role="img" aria-label="Photographer holding a camera" style="background:linear-gradient(160deg,#3a3a3a,#0e0e0e)"></div><div class="cap">Urber Photography</div></div>
<div class="abs thumb" style="left:734px"><div class="pic" role="img" aria-label="Dogs standing by a lake" style="background:linear-gradient(180deg,#5b8fc0,#6f8f5a 55%,#54704a)"></div><div class="cap">Urber Photography</div></div>
<div class="abs arrow left"></div>
<div class="abs arrow right"></div>
<div class="abs reflect" style="left:19px"></div>
<div class="abs reflect" style="left:162px"></div>
<div class="abs reflect" style="left:305px"></div>
<div class="abs reflect" style="left:448px"></div>
<div class="abs reflect" style="left:591px"></div>
<div class="abs reflect" style="left:734px"></div>

<div class="abs content"></div>

<h2 class="abs heading" style="left:9px;top:655px">Testimonial</h2>
<div class="abs" style="left:7px;top:687px;width:235px;height:182px;background:linear-gradient(150deg,#f2f2f2,#b9b9b9)" role="img" aria-label="Rolled certificate tied with a red ribbon"></div>
<p class="abs caption" style="left:7px;top:869px;width:235px;height:42px">Lorem Ipsum is simply dummy text of the and typesetting industry. <em>- Dana Reyes</em></p>

<h2 class="abs heading" style="left:9px;top:928px">Links</h2>
<ul class="abs links">
  <li>General Information</li>
  <li>Daily Shooting Times</li>
  <li>Nautical Twilight statt to end</li>
  <li>Moon face chart</li>
  <li>Link &amp; Review</li>
</ul>

<h2 class="abs heading" style="left:277px;top:655px">Blog</h2>
<div class="abs post" style="top:685px"><p class="post-title">Us Photography in 2012</p><span class="post-date">21st june,2012</span><p class="post-text">Lorem Ipsum is simply dummy text of the printing and typesetting indus-try. Lorem Ipsum has been the industry's standard dummy text ever</p></div>
<div class="abs post" style="top:761px"><p class="post-title">Us Photography in 2012</p><span class="post-date">21st june,2012</span><p class="post-text">Lorem Ipsum is simply dummy text of the printing and typesetting indus-try. Lorem Ipsum has been the industry's standard dummy text ever</p></div>
<div class="abs post" style="top:840px"><p class="post-title">Us Photography in 2012</p><span class="post-date">21st june,2012</span><p class="post-text">Lorem Ipsum is simply dummy text of the printing and typesetting indus-try. Lorem Ipsum has been the industry's standard dummy text ever</p></div>
<div class="abs post" style="top:920px"><p class="post-title">Us Photography in 2012</p><span class="post-date">21st june,2012</span><p class="post-text">Lorem Ipsum is simply dummy text of the printing and typesetting indus-try. Lorem Ipsum has been the industry's standard dummy text ever</p></div>
<div class="abs post" style="top:1000px"><p class="post-title">Us Photography in 2012</p><span class="post-date">21st june,2012</span><p class="post-text" style="border-bottom:none">Lorem Ipsum is simply dummy text of the printing and typesetting indus-try. Lorem Ipsum has been the industry's standard dummy text ever</p></div>

<h2 class="abs heading" style="left:647px;top:655px">Members Gallery</h2>
<div class="abs" style="left:645px;top:687px;width:235px;height:186px;background:linear-gradient(160deg,#4a3527,#9c7e60 60%,#6b5644)" role="img" aria-label="Goat grazing behind a wire fence"></div>
<p class="abs caption" style="left:645px;top:873px;width:235px;height:47px">Lorem Ipsum is simply dummy text of the print-ing and typesetting m Ipsum is simply dummy</p>

<h2 class="abs heading" style="left:647px;top:933px">Photographers Check List</h2>
<ul class="abs checks">
  <li><svg width="16" height="13" viewBox="0 0 16 13"><path d="M1 7l5 5L15 1" fill="none" stroke="#fff" stroke-width="3"/></svg>Wedding Check Lists</li>
  <li><svg width="16" height="13" viewBox="0 0 16 13"><path d="M1 7l5 5L15 1" fill="none" stroke="#fff" stroke-width="3"/></svg>Pre shoot Check Lists</li>
  <li><svg width="16" height="13" viewBox="0 0 16 13"><path d="M1 7l5 5L15 1" fill="none" stroke="#fff" stroke-width="3"/></svg>Standard Check Lists</li>
</ul>

<div class="abs footer"></div>
<div class="abs foot-brand"><div class="foot-dot"></div></div>
<p class="abs foot-copy">All Rights Reserved to Lens Compass</p>
<div class="abs follow">FOLLOW US ON
  <svg style="position:absolute;right:12px;top:8px" width="26" height="24" viewBox="0 0 26 24"><path d="M4 23L9 3" stroke="#ddd" stroke-width="2"/><path d="M9 3l14 3-4 6 3 6-13-3z" fill="#1f6fd0"/></svg>
</div>

</body>
</html>
```